御城印はほぼ形式が決まっており、
サイズは幅105mm×高さ160mmで、ハガキより少し縦長になります。
文言などはほぼ定型で、内容は「記載項目」に表記します。

記載項目
文言は、

国指定史跡
対馬
鷹巣岳城
令和 年 月 日

で、鷹巣岳城の背景に家紋(対馬菅氏の場合、四ツ目結)になります。
テキストは黒の筆文字が多く、家紋は朱色が多いです。
目的・デザインなどの参考に、以前作成した御城印の記事をリンクします。

楢崎城跡の「御城印」を作成 汐凪観光物産協会(長崎新聞2019/12/06)
https://hanabosi-kiji.example/839201457362018495
幅105mm×高さ160mm

御城印はほぼ様式が決まっており、アレンジが難しかったと思いますが、文字のフォント・サイズ・配置、家紋の加工や配置、背景画像等の提案、全体のバランス等を考慮し、決定いたしました。

今回2度目のデザミールの利用でしたが、力作ぞろいの個性的な提案をいただき、感謝申し上げます。
前回はWEBサイト制作、今回は御城印でしたが、リーフレットなど各種デザインをご依頼することもあると思います。
ありがとうございました。
今後ともよろしくお願いいたします。

```html
<!DOCTYPE html>
<html lang="ja">
<head>
<meta charset="utf-8">
<title>鷹巣岳城 御城印</title>
<link rel="stylesheet" href="https://fonts.googleapis.com/css2?family=Yuji+Boku&display=swap">
<style>
  :root {
    --paper: #ffffff;
    --ink: #111111;
    --crest-tone: #e0454c;
    --stone-dark: #8d8d8d;
    --stone-light: #e6e6e6;
    --trim: #555555;
  }
  html, body {
    margin: 0;
    padding: 0;
    width: 882px;
    height: 1200px;
    overflow: hidden;
    background: var(--paper);
  }
  .stamp {
    position: relative;
    width: 882px;
    height: 1200px;
    font-family: "Yuji Boku", serif;
    color: var(--ink);
  }
  .trim-marks, .stone-wall, .crest-area {
    position: absolute;
    left: 0;
    top: 0;
  }
  .vertical {
    position: absolute;
    writing-mode: vertical-rl;
    margin: 0;
    line-height: 1;
    font-weight: 400;
  }
  .designation {
    left: 608px;
    top: 84px;
    font-size: 62px;
    letter-spacing: 6px;
  }
  .region {
    left: 513px;
    top: 142px;
    font-size: 80px;
    letter-spacing: 4px;
  }
  .castle-name {
    left: 352px;
    top: 262px;
    font-size: 170px;
    letter-spacing: 6px;
  }
  .date-line {
    left: 194px;
    top: 192px;
    font-size: 50px;
    letter-spacing: 4px;
  }
  .date-line .blank {
    display: inline-block;
    height: 46px;
  }
</style>
</head>
<body>
<main class="stamp">
  <svg class="stone-wall" width="882" height="1200" role="img" aria-label="城跡の石垣の写真(モノクロ)">
    <defs>
      <linearGradient id="stoneTone" x1="0" y1="0" x2="0" y2="1">
        <stop offset="0" stop-color="var(--stone-dark)" stop-opacity="0.55"/>
        <stop offset="1" stop-color="var(--stone-light)" stop-opacity="0.5"/>
      </linearGradient>
    </defs>
    <path d="M118 720 L200 690 L300 650 L420 690 L560 680 L640 730 L720 790 L759 850 L759 1000 L640 1010 L420 1020 L250 1015 L118 1000 Z" fill="url(#stoneTone)"/>
  </svg>

  <svg class="trim-marks" width="882" height="1200" fill="none" stroke="var(--trim)" stroke-width="1.2" aria-hidden="true">
    <path d="M60 132 H118 M118 74 V132 M60 100 H88 M88 74 V100"/>
    <path d="M822 132 H764 M764 74 V132 M822 100 H794 M794 74 V100"/>
    <path d="M60 1111 H118 M118 1169 V1111 M60 1140 H88 M88 1169 V1140"/>
    <path d="M822 1111 H764 M764 1169 V1111 M822 1140 H794 M794 1169 V1140"/>
    <path d="M441 74 V122 M400 100 H482"/>
    <path d="M441 1120 V1169 M400 1140 H482"/>
    <path d="M60 621 H108 M80 580 V662"/>
    <path d="M774 621 H822 M802 580 V662"/>
  </svg>

  <svg class="crest-area" width="882" height="1200" role="img" aria-label="家紋(四ツ目結・朱色)の配置箇所">
    <rect x="333" y="430" width="216" height="216" fill="var(--crest-tone)" opacity="0.85"/>
  </svg>

  <h2 class="vertical designation">国指定史跡</h2>
  <h2 class="vertical region">対馬</h2>
  <h1 class="vertical castle-name">鷹巣岳城</h1>
  <p class="vertical date-line">令和<span class="blank"></span>年<span class="blank"></span>月<span class="blank"></span>日</p>
</main>
</body>
</html>
```